依頼詳細
海外のセルフサービス式飲食店で使用します。各商品の前につける値札の作成をお願します。

Karaage Chicken $2.8
炸鸡
가라아게 치킨
鶏の唐揚げ
Pollo frito

こちらの商品の値札のデザイン作成していただき、採用決定後に、デザインはそのままその他約60品の商品名や金額の入力をお願いさせて頂きたいと思っています。

英語をメインに
日本語、中国語、韓国語、スペイン語
も併記したく思っています。

英語圏(オーストラリア)にある日本食レストランですので英語の次に日本語が大きくなって、他3ヶ国語が小さくても構いません。

サイズは" 3.5cm x 6cm "
でお願いいたします。

納品の際には、イラストレーターまたはフォトショップで文字の編集が可能なデータをお願いします。

ロゴを添付しています。
ロゴは有り、無し、または ロゴ内のキャラクター部分のみの使用でも構いません。ロゴの色や印象に合うデザインを希望しています。

よろしくお願いいたします。
記載項目

商品名:Karaage Chicken
価格:$2.8
日本語:鶏の唐揚げ
中国語:炸鸡
韓国語:가라아게 치킨
スペイン語:Pollo frito

ベジタリアンの商品にはベジタリアン商品と伝わるようなマーク
サイズ
3.5cm x 6cm
ページ数
片面
希望イメージ
シンプル 複雑
単色 カラフル
暗い 明るい
日常 高級
遊び心 厳粛
未来的 伝統的
女性的 男性的
希望する色
黄・オレンジ系

シンプルで見やすいのでこちらを選ばせて頂きました!

この度はご応募いただきありがとうございます。素敵なデザインを数々ご提案いただきましたが一つに絞らせていただきました。

また今後機会がありましたらよろしくお願いいたします

```html
<!DOCTYPE html>
<html lang="ja">
<head>
<meta charset="utf-8">
<title>Karaage Chicken 値札</title>
<link rel="stylesheet" href="https://fonts.googleapis.com/css2?family=M+PLUS+Rounded+1c:wght@500;800&family=Noto+Sans+KR:wght@500&display=swap">
<style>
  :root {
    --page: #ffffff;
    --tag-bg: #f6e89a;
    --tag-edge: #ecd46a;
    --title: #d9861a;
    --ink: #1e1a14;
    --label-bg: #ffffff;
    --food-main: #f3c95a;
    --food-light: #fbe7a6;
    --dot-jp: #d8262c;
    --dot-cn: #e23a1e;
    --dot-kr: #3a5fb0;
    --dot-es: #e6a21a;
  }
  html, body {
    margin: 0;
    padding: 0;
    width: 857px;
    height: 1200px;
    overflow: hidden;
    background: var(--page);
  }
  .price-tag {
    position: absolute;
    left: 309px;
    top: 206px;
    width: 242px;
    height: 145px;
    background: var(--tag-bg);
    border: 1px solid var(--tag-edge);
    box-sizing: border-box;
    font-family: "M PLUS Rounded 1c", sans-serif;
    color: var(--ink);
    overflow: hidden;
  }
  .product-name {
    position: absolute;
    left: 0;
    right: 0;
    top: 6px;
    margin: 0;
    text-align: center;
    font-size: 21px;
    font-weight: 800;
    color: var(--title);
    letter-spacing: 0.2px;
    line-height: 1;
    white-space: nowrap;
  }
  .price-label {
    position: absolute;
    left: 28px;
    top: 37px;
    width: 120px;
    height: 26px;
    background: var(--label-bg);
    border-radius: 4px;
    display: flex;
    align-items: center;
    justify-content: center;
    font-size: 16px;
    font-weight: 800;
    white-space: nowrap;
  }
  .translations {
    position: absolute;
    left: 11px;
    top: 68px;
    margin: 0;
    padding: 0;
    list-style: none;
    font-size: 9px;
    font-weight: 500;
    line-height: 17px;
    z-index: 1;
  }
  .translations li {
    display: flex;
    align-items: center;
    gap: 4px;
    white-space: nowrap;
    height: 17px;
  }
  .translations .dot {
    width: 8px;
    height: 8px;
    border-radius: 50%;
    flex: none;
  }
  .dot-jp { background: var(--dot-jp); }
  .dot-cn { background: var(--dot-cn); }
  .dot-kr { background: var(--dot-kr); }
  .dot-es { background: var(--dot-es); }
  .translations .lang {
    display: inline-block;
    width: 46px;
    flex: none;
    white-space: nowrap;
    text-align: justify;
    text-align-last: justify;
  }
  .translations .kr { font-family: "Noto Sans KR", sans-serif; }
  .food-art {
    position: absolute;
    left: 120px;
    top: 51px;
    width: 118px;
    height: 92px;
  }
</style>
</head>
<body>
  <section class="price-tag">
    <h1 class="product-name">Karaage Chicken</h1>
    <div class="price-label">価格 : $2.8</div>
    <svg class="food-art" viewBox="0 0 118 92" role="img" aria-label="Illustration of fried karaage chicken pieces with chopsticks">
      <defs>
        <radialGradient id="foodTone" cx="50%" cy="55%" r="55%">
          <stop offset="0" stop-color="#fbe7a6"/>
          <stop offset="1" stop-color="#f3c95a"/>
        </radialGradient>
      </defs>
      <ellipse cx="70" cy="62" rx="44" ry="27" fill="url(#foodTone)"/>
    </svg>
    <ul class="translations">
      <li><span class="dot dot-jp"></span><span class="lang">日本語</span>: 鶏の唐揚げ</li>
      <li><span class="dot dot-cn"></span><span class="lang">中国語</span>: 炸鸡</li>
      <li><span class="dot dot-kr"></span><span class="lang">韓国語</span>: <span class="kr">가라아게 치킨</span></li>
      <li><span class="dot dot-es"></span><span class="lang">スペイン語</span>: Pollo frito</li>
    </ul>
  </section>
</body>
</html>
```